Wordpress Design for Fruit & Veggie Swap Site

I need a wordpress design for the HOME PAGE of a company located in Kona, Hawaii called Leaf Loop Hawaii. Leaf Loop Hawaii (LLH) is a site intended to support the local food movement by connecting neighbors in order for them to swap/trade produce from their farm or garden. The purpose of this site is to support sustainable agriculture in Hawaii and encourage community interaction.

The model of the site is similar to:
http://www.harvtrade.me/ (I really like the simple design of this site)
http://www.plotbarter.co.uk/ (I don't like the design of this site, just the functionality. The design is too busy and unbalanced.)
Unlike the two sites listed above, however, LLH is only targeted at people living on the Big Island of Hawaii.

The site is simply intended to be a platform to connect people, then they are free to swap or barter off site, similar to the way tradeboard connects people. Users can create "posts" for crops that they have available for swap, which are searchable based on name and location.

I have created a very basic, no-css, dev version of the site to work on the back end, which is located here: http://leafloophawaii.com/test
Feel free to register and create a test post to get a feel for how it works.

The images I have uploaded are just for ideas and do not have to be in the design.
Updates

Reason: I extended the deadline so you have more time to work on designs. Thank you!

Target Market(s)

The targeted audience is gardeners and farmers on the Big Island of Hawaii. These people are quite varied in age and technical ability.

Industry/Entity Type

Agriculture

Requirements
Must have
• On the homepage, I would like to have a list of the most recent "posts", displayed as the post title, with the most recent post at the top of the list. In the test site, this is located in the right column, but it doesn't have to be in that location in the final design.

I would also like the option to "Add new listing" to be displayed creatively on the home page. This can be in the form of a graphic that links to a form on another page.

I would also like to have a search box on the homepage. Users can search by crop name and/or location.

The main focal point of the home page will be a Google map application of the Big Island. I am in the process of developing this. You can see the map on the test site, please keep in mind that this map may change slightly in future revisions. Feel free to change the size and styling of the map to fit your design.

I would like the homepage to have a simple and clean layout, making it clear to users how the site works.
For the graphics, I would like to incorporate the "crop circles" idea (yes, like the alien crop circles in fields) with fruits and veggies (including tropical fruit found in Hawaii like banana, coconut, lychee, taro, oranges, as well as traditional vegetables like carrots, lettuce, etc.), and also potentially with the idea of sharing and circulating produce with neighbors.
Please note that those specific fruits and veggies don't need to be used, or that many of them, I was just giving them as examples.

I would also like to have a place on the homepage where users can login/sign up. This can be a login form with a sign up link, or a login link and a sign up link.

I would like the entire design to fit on a page without having to scroll.

Once the site has a substantial user base, I plan to incorporate advertising. Please create a design that will be easy to integrate ads into in the future, most likely in the side bar or footer. I do not want the original design to have ad space, just the ability to add it easily in the future and having it look good with the current design.

```html
<!DOCTYPE html>
<html lang="en">
<head>
<meta charset="utf-8">
<title>Leaf Loop Hawaii — Home</title>
<link rel="stylesheet" href="https://fonts.googleapis.com/css2?family=Fredoka:wght@500;600&family=Open+Sans:wght@400;600;700&family=Arimo:wght@400;700&display=swap">
<style>
  :root {
    --band-dark: #2f2f2f;
    --band-dark-2: #363636;
    --paper: #ffffff;
    --mist: #e4e4e4;
    --ink: #4a4a4a;
    --ink-soft: #666666;
    --heading: #4d4d4d;
    --orange: #ee6c0b;
    --orange-light: #f8922a;
    --green: #5f8a1c;
    --olive: #7d8f2c;
    --olive-light: #9aab45;
    --lime: #8fd22a;
    --lime-dark: #5fa810;
    --line: #dcdcdc;
    --field: #111111;
  }
  * { box-sizing: border-box; margin: 0; padding: 0; }
  html, body { width: 1200px; height: 1099px; overflow: hidden; }
  body {
    position: relative;
    font-family: "Open Sans", Arial, sans-serif;
    color: var(--ink);
    background:
      linear-gradient(to bottom, var(--band-dark) 0, var(--band-dark-2) 342px, var(--mist) 342px, #f7f7f7 380px, var(--paper) 400px);
  }
  .abs { position: absolute; }

  /* Brand */
  .brand { left: 140px; top: 38px; display: flex; align-items: center; gap: 12px; }
  .brand-dot { width: 48px; height: 48px; border-radius: 50%; background: var(--olive-light); }
  .brand-name { font-family: "Fredoka", sans-serif; font-weight: 600; font-size: 30px; color: #ffffff; }

  /* Account */
  .account { left: 742px; top: 17px; width: 320px; font-size: 12.5px; color: #cfcfcf; }
  .account .fields { display: flex; gap: 10px; }
  .account .field {
    width: 155px; height: 26px; background: var(--field); border: 1px solid #444;
    color: #bdbdbd; font-style: italic; font-size: 13px; padding: 4px 9px;
  }
  .account .options { display: flex; gap: 18px; margin-top: 10px; }
  .account .option { display: flex; align-items: center; gap: 8px; }
  .tick { width: 12px; height: 12px; background: #e6e6e6; border-radius: 2px; display: inline-block; position: relative; }
  .tick svg { position: absolute; left: 1px; top: 1px; }
  .account .actions { display: flex; align-items: center; gap: 16px; margin-top: 11px; }
  .btn-signin {
    width: 90px; height: 29px; border-radius: 3px; border: 1px solid #4b8a0c;
    background: linear-gradient(var(--lime), var(--lime-dark));
    color: #1f3a05; font-family: "Arimo", sans-serif; font-weight: 700; font-size: 14px;
    display: flex; align-items: center; justify-content: center;
  }
  .signup-link { color: #ffffff; text-decoration: underline; font-size: 13.5px; }
  .or { font-size: 13px; color: #bbb; }

  /* Navigation */
  .nav {
    left: 140px; top: 124px; width: 920px; height: 48px; background: linear-gradient(#ffffff, #f1f1f1);
    border-radius: 7px 7px 0 0; display: flex; align-items: center;
    font-family: "Arimo", sans-serif; font-weight: 700; font-size: 15.5px; color: #333;
  }
  .nav a { position: absolute; top: 13px; color: #333; text-decoration: none; }
  .nav a.active {
    top: 10px; left: 15px; height: 27px; padding: 4px 14px; border-radius: 14px;
    background: linear-gradient(var(--orange-light), var(--orange)); color: #fff;
  }
  .search {
    position: absolute; left: 692px; top: 10px; width: 212px; height: 27px;
    border: 1px solid #cfcfcf; border-radius: 14px; background: #fff;
    font-family: "Open Sans", sans-serif; font-weight: 400; font-style: italic; font-size: 13px; color: #777;
    padding: 4px 12px;
  }
  .search-btn {
    position: absolute; right: -1px; top: -1px; width: 30px; height: 27px; border-radius: 0 14px 14px 0;
    background: linear-gradient(var(--orange-light), var(--orange)); display: flex; align-items: center; justify-content: center;
  }

  /* Hero */
  .hero {
    left: 140px; top: 172px; width: 920px; height: 316px; border-radius: 0 0 7px 7px; overflow: hidden;
    background: linear-gradient(100deg, #9fb35a 0%, #c4d07e 22%, #dfe4cd 40%, #eeeeea 60%, #f4f4f2 100%);
    box-shadow: 0 4px 8px rgba(0,0,0,.15);
  }
  .hero-fruit {
    position: absolute; left: 574px; top: 212px; width: 320px; height: 104px; border-radius: 50px 50px 0 0;
    background: linear-gradient(90deg, #d9cbb0, #c48f3a 40%, #e29a2c 70%, #a9c24a);
  }
  .hero-title {
    position: absolute; left: 500px; top: 56px; width: 300px; text-align: center;
    font-family: "Fredoka", sans-serif; font-weight: 600; line-height: 1;
  }
  .hero-title .l1 { font-size: 38px; color: var(--orange); }
  .hero-title .l1 span { color: var(--green); }
  .hero-title .l2 { font-size: 32px; color: var(--orange); margin-top: 1px; }
  .hero-sub { position: absolute; left: 470px; top: 138px; width: 340px; text-align: center; font-size: 16.5px; line-height: 19px; color: #444; }

  /* Welcome */
  .welcome { left: 140px; top: 518px; width: 620px; }
  .section-title { font-family: "Fredoka", sans-serif; font-weight: 500; color: var(--heading); }
  .welcome h1 { font-size: 35px; }
  .welcome h1 span { color: var(--orange); }
  .welcome p { margin-top: 8px; font-size: 15px; line-height: 21px; color: var(--ink-soft); }
  .read-more {
    left: 662px; top: 638px; width: 96px; height: 25px; border-radius: 13px; border: 1px solid #e6e6e6;
    box-shadow: 0 2px 2px rgba(0,0,0,.08); background: #fff; font-size: 12px; color: var(--orange);
    display: flex; align-items: center; justify-content: center; gap: 6px;
  }
  .here h2 { font-size: 27px; }
  .map-frame { left: 140px; top: 724px; width: 620px; height: 161px; border: 1px solid #d5d5d5; padding: 4px; background: #fff; }
  .map-area { width: 100%; height: 100%; background: radial-gradient(ellipse 90px 70px at 48% 50%, #cfe1bd 0 70%, #a9c2de 72%); }

  /* Sidebar */
  .recent-head {
    left: 797px; top: 527px; width: 264px; height: 42px; border-radius: 4px 4px 0 0;
    background: linear-gradient(var(--olive-light), var(--olive));
    font-family: "Fredoka", sans-serif; font-weight: 500; font-size: 25px; color: #fff; padding: 5px 17px;
  }
  .recent-notch { left: 833px; top: 569px; }
  .post { left: 797px; width: 264px; height: 86px; border-bottom: 1px dotted #cfcfcf; }
  .post:last-of-type { border-bottom: none; }
  .post .thumb { position: absolute; left: 5px; top: 22px; width: 44px; height: 44px; border-radius: 50%; }
  .post .title { position: absolute; left: 65px; top: 10px; font-size: 17.5px; color: var(--orange); line-height: 21px; }
  .post .title small { font-size: 15px; color: var(--olive); }
  .post .excerpt { position: absolute; left: 66px; width: 196px; font-size: 12.5px; line-height: 17px; color: var(--ink-soft); }
  .view-all {
    left: 797px; top: 854px; width: 264px; height: 29px; background: #efefef; border-radius: 5px;
    font-size: 13.5px; color: var(--olive); padding: 5px 19px;
  }

  /* Footer */
  .footer { left: 0; top: 954px; width: 1200px; height: 145px; background: var(--band-dark); }
  .cta {
    left: 238px; top: 922px; width: 714px; height: 62px; border-radius: 31px; border: 3px solid #fff;
    background: linear-gradient(#555, #2c2c2c); box-shadow: 0 2px 6px rgba(0,0,0,.35); overflow: hidden;
  }
  .cta-text { position: absolute; left: 40px; top: 10px; font-family: "Arimo", sans-serif; font-weight: 700; font-size: 30px; color: #fff; }
  .cta-btn {
    position: absolute; right: 0; top: 0; width: 270px; height: 100%; border-radius: 28px;
    background: linear-gradient(var(--orange-light), #d45a05);
    font-family: "Arimo", sans-serif; font-weight: 700; font-size: 24px; color: #fff;
    display: flex; align-items: center; justify-content: center; gap: 14px;
  }
  .footer-links { left: 140px; top: 1014px; display: flex; font-size: 14px; color: #e5e5e5; }
  .footer-links span { padding: 0 10px; border-left: 1px solid #666; }
  .footer-links span:first-child { padding-left: 0; border-left: none; }
  .copyright { left: 140px; top: 1050px; font-size: 14px; color: #e5e5e5; }
  .follow { left: 971px; top: 1014px; font-size: 14px; color: #e5e5e5; }
  .social { top: 1042px; width: 30px; height: 30px; border-radius: 4px; }
  .social.one { left: 972px; background: #3b5a98; }
  .social.two { left: 1012px; background: #4aa9e4; }
</style>
</head>
<body>

  <div class="abs brand">
    <span class="brand-dot"></span>
    <span class="brand-name">Leaf Loop Hawaii</span>
  </div>

  <form class="abs account">
    <div class="fields">
      <div class="field">Your email</div>
      <div class="field">Password</div>
    </div>
    <div class="options">
      <span class="option"><span class="tick"><svg width="10" height="10" viewBox="0 0 10 10"><path d="M1.5 5l2.5 2.5 4.5-5" stroke="#333" stroke-width="1.6" fill="none"/></svg></span>Forgot your password?</span>
      <span class="option"><span class="tick"><svg width="10" height="10" viewBox="0 0 10 10"><path d="M1.5 5l2.5 2.5 4.5-5" stroke="#333" stroke-width="1.6" fill="none"/></svg></span>Create New Account</span>
    </div>
    <div class="actions">
      <span class="btn-signin">SIGN IN</span>
      <span class="or">or <a class="signup-link">Sign Up</a></span>
    </div>
  </form>

  <nav class="abs nav">
    <a class="active">HOME</a>
    <a style="left:100px">ABOUT US</a>
    <a style="left:200px">BLOG</a>
    <a style="left:266px">FORUM</a>
    <a style="left:346px">GARDERN SHOP</a>
    <a style="left:486px">CONTACT US</a>
    <div class="search">Enter crop name
      <span class="search-btn"><svg width="14" height="14" viewBox="0 0 14 14"><circle cx="5.5" cy="5.5" r="4" stroke="#fff" stroke-width="2" fill="none"/><path d="M8.5 8.5l4 4" stroke="#fff" stroke-width="2.2"/></svg></span>
    </div>
  </nav>

  <section class="abs hero">
    <div role="img" aria-label="Photo of a bunch of green grapes on the vine against a soft light background" style="position:absolute;inset:0"></div>
    <div class="hero-fruit" role="img" aria-label="Split coconut beside a pile of tropical fruit: grapes, bananas, oranges, kiwi and apple"></div>
    <div class="hero-title">
      <div class="l1">Your <span>Garden is</span></div>
      <div class="l2">Bigger with Friends</div>
    </div>
    <p class="hero-sub">Barter and trade or buy &amp; sell crops<br>with your neighbors.</p>
  </section>

  <section class="abs welcome">
    <h1 class="section-title">Welcome to <span>Leaf Loop Hawaii</span></h1>
    <p>Lorem Ipsum is simply dummy text of the printing and typesetting industry. Lorem Ipsum has been the industry's standard dummy text ever since the 1500s, when an unknown printer took a galley of type and scrambled.</p>
  </section>
  <a class="abs read-more">Read More <svg width="12" height="12" viewBox="0 0 12 12"><circle cx="6" cy="6" r="5" stroke="#ee6c0b" fill="none"/><path d="M5 3.5L7.5 6 5 8.5" stroke="#ee6c0b" fill="none"/></svg></a>

  <section class="abs here" style="left:140px;top:680px">
    <h2 class="section-title">Here we have</h2>
  </section>
  <div class="abs map-frame">
    <div class="map-area" role="img" aria-label="Map of the Big Island of Hawaii with red pins marking crop listings"></div>
  </div>

  <aside>
    <div class="abs recent-head">Recent Post</div>
    <svg class="abs recent-notch" width="18" height="10" viewBox="0 0 18 10"><path d="M0 0h18L9 10z" fill="#7d8f2c"/></svg>

    <div class="abs post" style="top:576px">
      <div class="thumb" role="img" aria-label="Halved coconut" style="background:radial-gradient(circle,#f3ece2 40%,#6b4a2f 45%)"></div>
      <div class="title">COCONUT <small>(hilo)</small></div>
      <div class="excerpt" style="top:35px">Lorem Ipsum is simply dummy to text of the printing</div>
    </div>
    <div class="abs post" style="top:662px">
      <div class="thumb" role="img" aria-label="Ripe mango" style="background:radial-gradient(circle at 40% 40%,#ffd23a,#e8950f)"></div>
      <div class="title">MANGO <small>(pahoa)</small></div>
      <div class="excerpt" style="top:35px">Lorem Ipsum is simply dummy to text of the printing</div>
    </div>
    <div class="abs post" style="top:748px;height:100px">
      <div class="thumb" role="img" aria-label="Steaming cup of coffee" style="background:radial-gradient(circle,#6b3d1e 45%,#c7dfa0 50%)"></div>
      <div class="title">COFFEE CHERRIES<br><small>(kapoho)</small></div>
      <div class="excerpt" style="top:56px">Lorem Ipsum is simply dummy to text of the printing</div>
    </div>
    <div class="abs view-all">View All ›</div>
  </aside>

  <footer class="abs footer"></footer>
  <div class="abs cta">
    <span class="cta-text">How Something to share?</span>
    <span class="cta-btn">ADD NEW LISTING <svg width="10" height="16" viewBox="0 0 10 16"><path d="M2 2l6 6-6 6" stroke="#fff" stroke-width="2.4" fill="none"/></svg></span>
  </div>
  <div class="abs footer-links">
    <span>Home</span><span>About Us</span><span>Blog</span><span>Forum</span><span>Garden Shop</span><span>Contact Us</span>
  </div>
  <div class="abs copyright">Copyright © 2013 Leaf Loop Hawaii.&nbsp; All Rights Reserved.</div>
  <div class="abs follow">FolloW Us On</div>
  <span class="abs social one"></span>
  <span class="abs social two"></span>

</body>
</html>
```